Business Card Design Project

We require a professional business card designed for our consulting organisation that has the same theme and colours as our logo except for the grey.

Colours on the front should predominately be white however some reference to our logo colours except for the grey.

The back of the card should be have background colour that aligns with our logo colour.

Layout, style and design is up to the designer. So send through your designs

Details are attached in the word document project brief.

Target Market(s)

Target market are large corporate organisations

Industry/Entity Type

Business

Requirements
Must have
• Content on the front must have:

Dean Halvorsen
Managing Director

P: 0417 285 394
E: Dean@brevolinkpartners.com
W: www.brevolinkpartners.com

Content on the back must have the words:
Alliances
Placement
Training
Support

Design Colours
Must align to our logo

```html
<!DOCTYPE html>
<html lang="en">
<head>
<meta charset="utf-8">
<title>Brevolink Partners – Business Card</title>
<link href="https://fonts.googleapis.com/css2?family=Noto+Sans:wght@400;600;700&family=Roboto+Condensed:wght@400&display=swap" rel="stylesheet">
<style>
  :root {
    --stage: #262525;
    --card: #ffffff;
    --brand-blue: #2878be;
    --brand-blue-soft: #2f82c6;
    --brand-deep: #1f6db4;
    --mark-faint: #b3cde6;
    --text-light: #ffffff;
    --bullet: #7f8c99;
    --label: #ffffff;
  }
  * { margin: 0; padding: 0; box-sizing: border-box; }
  html, body { width: 1200px; height: 900px; overflow: hidden; background: var(--stage); }
  .stage { position: relative; width: 1200px; height: 900px; font-family: "Noto Sans", sans-serif; }

  .side-label {
    position: absolute; left: 120px;
    font-family: "Roboto Condensed", sans-serif;
    font-size: 40px; color: var(--label);
  }
  .side-label--front { top: 206px; }
  .side-label--back { top: 656px; }

  .card {
    position: absolute; left: 345px; width: 759px; height: 433px;
    background: var(--card);
  }
  .card--front { top: 9px; }
  .card--back { top: 457px; }

  .brand {
    position: absolute; left: 70px; top: 36px; width: 640px; height: 150px;
    display: flex; align-items: center; gap: 80px;
  }
  .brand__dot { width: 120px; height: 120px; border-radius: 50%; background: var(--brand-deep); flex: none; }
  .brand__name {
    font-weight: 600; font-size: 64px; line-height: 66px;
    color: var(--brand-deep); letter-spacing: 1px;
  }
  .card--back .brand__dot { background: var(--mark-faint); }
  .card--back .brand__name { color: var(--mark-faint); }

  .band {
    position: absolute; left: 14px; top: 215px; width: 732px; height: 180px;
    background: radial-gradient(ellipse at 50% 0%, var(--brand-blue-soft) 0%, var(--brand-blue) 70%);
    overflow: hidden;
    box-shadow: 0 1px 2px rgba(0,0,0,0.25);
  }
  .card--back .band { top: 214px; height: 179px; }

  .contact {
    position: absolute; inset: 0; text-align: center;
    color: var(--text-light); font-size: 16px; line-height: 20px; padding-top: 21px;
  }
  .contact__name { font-weight: 700; }
  .contact__gap { height: 19px; }

  .services {
    position: absolute; inset: 0; list-style: none;
    color: var(--text-light); font-size: 22px;
  }
  .services li { position: absolute; padding-left: 17px; }
  .services li::before {
    content: ""; position: absolute; left: 0; top: 13px;
    width: 6px; height: 6px; background: var(--bullet);
  }
</style>
</head>
<body>
<main class="stage">
  <div class="side-label side-label--front">Front</div>
  <div class="side-label side-label--back">Back</div>

  <section class="card card--front">
    <div class="brand">
      <span class="brand__dot"></span>
      <span class="brand__name">Brevolink<br>Partners</span>
    </div>
    <div class="band">
      <div class="contact">
        <div class="contact__name">Dean Halvorsen</div>
        <div>Managing Director</div>
        <div class="contact__gap"></div>
        <div>P: 0417 285 394</div>
        <div>E: Dean@brevolinkpartners.com</div>
        <div class="contact__gap"></div>
        <div>W: www.brevolinkpartners.com</div>
      </div>
    </div>
  </section>

  <section class="card card--back">
    <div class="brand">
      <span class="brand__dot"></span>
      <span class="brand__name">Brevolink<br>Partners</span>
    </div>
    <div class="band">
      <ul class="services">
        <li style="left:173px; top:52px;">Alliances</li>
        <li style="left:173px; top:90px;">Placement</li>
        <li style="left:470px; top:52px;">Training</li>
        <li style="left:470px; top:92px;">Support</li>
      </ul>
    </div>
  </section>
</main>
</body>
</html>
```